Engineering Consultant Business Card

I'm starting a new business as a high-end engineering consultant in a niche field. I've attached the jpg for my logo plus the branding guideline document that I've been following. You can see my business website here: www.tarvikworks.com
I'd like a business card that has the logo on one side, then the other side has (in any order): Tarvik Works, Inc.
Dana Whitlock
President and Chief EMC Engineer
www.tarvikworks.com
dana@tarvikworks.com
Optional: motto "We will solve your EMC problems as early as possible—ideally before they even start."
I'm not planning on including a phone number
Target Market(s)
Businesses, especially makers of electronics hardware
Industry/Entity Type
Electrical engineering
Contact Information for Business Card
Company name, my name, website, email

```html
<!DOCTYPE html>
<html lang="en">
<head>
<meta charset="utf-8">
<title>Tarvik Works – Business Card</title>
<link href="https://fonts.googleapis.com/css2?family=Rubik:wght@400;500;600;700;800&display=swap" rel="stylesheet">
<style>
  :root {
    --backdrop: #dde3e7;
    --brand-blue: #2b4899;
    --brand-cyan: #12a9cc;
    --card-white: #ffffff;
  }
  * { margin: 0; padding: 0; box-sizing: border-box; }
  html, body {
    width: 1200px; height: 1200px; overflow: hidden;
    background: var(--backdrop);
    font-family: "Rubik", Arial, sans-serif;
  }
  .canvas { position: relative; width: 1200px; height: 1200px; }
  .card { position: absolute; left: 315px; width: 570px; height: 369px; overflow: hidden; }
  .card--front {
    top: 190px; background: var(--brand-blue);
    display: flex; align-items: center; justify-content: center; gap: 18px;
  }
  .front-mark { width: 40px; height: 40px; border: 5px solid var(--card-white); border-radius: 50%; }
  .front-name { color: var(--card-white); font-size: 46px; font-weight: 600; letter-spacing: 0.5px; }

  .card--back { top: 640px; background: var(--card-white); color: var(--brand-blue); }
  .company { position: absolute; right: 23px; top: 29px; font-size: 24px; font-weight: 600; }
  .person-name { position: absolute; left: 63px; top: 105px; font-size: 35px; font-weight: 500; color: var(--brand-cyan); }
  .person-title { position: absolute; left: 63px; top: 152px; font-size: 15.5px; font-weight: 500; }
  .contact { position: absolute; left: 59px; list-style: none; }
  .contact li { display: flex; align-items: center; height: 29px; font-size: 21px; }
  .contact svg { width: 20px; height: 16px; margin-right: 11px; }
  .contact { top: 224px; }

  .motto { position: absolute; left: 397px; top: 120px; width: 150px; line-height: 1; }
  .motto span { display: block; }
  .motto__lead { font-size: 13.5px; font-weight: 500; }
  .motto__key { font-size: 68px; font-weight: 800; letter-spacing: -1px; margin-top: 2px; margin-left: -2px; }
  .motto__noun { font-size: 25.5px; font-weight: 800; margin-top: 1px; }
  .motto__time { font-size: 13.5px; font-weight: 500; margin-top: 6px; }
  .motto__aside { font-size: 9.5px; color: var(--brand-cyan); margin-top: 7px; }
</style>
</head>
<body>
<main class="canvas">
  <section class="card card--front" aria-label="Card front">
    <span class="front-mark" aria-hidden="true"></span>
    <span class="front-name">Tarvik Works</span>
  </section>

  <section class="card card--back" aria-label="Card back">
    <p class="company">Tarvik Works, Inc.</p>
    <h1 class="person-name">Dana Whitlock</h1>
    <p class="person-title">President and Chief EMC Engineer</p>
    <ul class="contact">
      <li>
        <svg viewBox="0 0 20 16" aria-hidden="true">
          <rect x="1" y="1" width="17" height="12" rx="1.5" fill="none" stroke="var(--brand-cyan)" stroke-width="2"/>
          <rect x="1" y="1" width="17" height="3.5" fill="var(--brand-cyan)"/>
          <path d="M11 8 L18 11 L15 12 L17 15 L15.5 16 L13.5 13 L11.5 15 Z" fill="var(--brand-blue)"/>
        </svg>www.tarvikworks.com
      </li>
      <li>
        <svg viewBox="0 0 20 16" aria-hidden="true">
          <rect x="1" y="2" width="18" height="12" fill="var(--brand-cyan)"/>
          <path d="M1 2 L10 9 L19 2 M1 14 L8 8 M19 14 L12 8" fill="none" stroke="var(--card-white)" stroke-width="1.4"/>
        </svg>dana@tarvikworks.com
      </li>
    </ul>
    <p class="motto">
      <span class="motto__lead">WE WILL SOLVE YOUR</span>
      <span class="motto__key">EMC</span>
      <span class="motto__noun">PROBLEMS</span>
      <span class="motto__time">AS EARLY AS POSSIBLE</span>
      <span class="motto__aside">—ideally before they even start.</span>
    </p>
  </section>
</main>
</body>
</html>
```